Modern card design needed for building development company

We are looking for a sharp modern new look for our business cards.
We are a New Zealand based company called TKV Ventures NZ LTD that specialises in subdividing large sections, housing and commercial buildings.
We have attached a photo of the current logo and would like to see it improved somehow as it looks a bit dated.
We are open to any colours.

Target Market(s)

Investors, Property buyers

Industry/Entity Type

Investment

Contact Information for Business Card

TKV VENTURES NZ LTD
www.tkvventuresnz.co.nz

Howard Pennick
Phone +64 21 843 192
Email hdpennick@fernmail.co.nz

Font styles to use
Serif
Sans Serif

Colors
0792cd
33a6d7
85cae6
6b449b
886aae
f04a50
ec1f27
f37122
f68d4d

Requirements
Must have
• Please try and make the logo more modern or if you have a similar one we would like to see it.

```html
<!DOCTYPE html>
<html lang="en">
<head>
<meta charset="utf-8">
<title>TKV Ventures NZ LTD – Business Card</title>
<link rel="stylesheet" href="https://fonts.googleapis.com/css2?family=Montserrat:wght@500;600;700&family=Work+Sans:wght@300;400&display=swap">
<style>
  :root {
    --maroon: #8c1727;
    --white: #ffffff;
    --backdrop: #e9e6e2;
    --shadow: rgba(0, 0, 0, 0.22);
  }
  * { margin: 0; padding: 0; box-sizing: border-box; }
  html, body { width: 1200px; height: 930px; overflow: hidden; }
  body { background: var(--backdrop); position: relative; font-family: "Work Sans", Arial, sans-serif; }

  .card {
    position: absolute;
    left: 278px;
    width: 644px;
    height: 370px;
    box-shadow: 0 6px 18px var(--shadow);
    overflow: visible;
  }
  .card--front { top: 75px; background: var(--white); }
  .card--back { top: 486px; background: var(--maroon); }

  .front__brand-side {
    position: absolute; left: 0; top: 0; width: 322px; height: 370px;
    display: flex; flex-direction: column; align-items: center; justify-content: center;
  }
  .front__info-side {
    position: absolute; left: 322px; top: 0; width: 322px; height: 370px;
    background: var(--maroon); color: var(--white);
  }
  .front__notch {
    position: absolute; left: -1px; top: 90px; width: 24px; height: 48px;
    background: var(--white);
    clip-path: polygon(0 0, 100% 50%, 0 100%);
  }

  .brand { display: flex; flex-direction: column; align-items: center; gap: 14px; }
  .brand__square { width: 46px; height: 46px; }
  .brand__name {
    font-family: "Montserrat", Arial, sans-serif; font-weight: 600;
    font-size: 13px; letter-spacing: 2.6px; white-space: nowrap;
  }
  .brand--dark .brand__square { background: var(--maroon); }
  .brand--dark .brand__name { color: #3a2a2c; }
  .brand--light .brand__square { background: var(--white); width: 60px; height: 60px; }
  .brand--light .brand__name { color: var(--white); font-size: 16px; letter-spacing: 3.2px; }

  .card--back .brand {
    position: absolute; left: 0; top: 0; width: 100%; height: 100%;
    justify-content: center; gap: 18px;
  }

  .contact { position: absolute; left: 34px; top: 88px; }
  .contact__name {
    font-family: "Montserrat", Arial, sans-serif; font-weight: 700;
    font-size: 23px; letter-spacing: 0.6px; line-height: 1.1;
  }
  .contact__role { font-weight: 300; font-size: 16px; line-height: 20px; margin-top: 2px; }
  .contact__address { font-weight: 300; font-size: 16px; line-height: 20.5px; margin-top: 11px; }
  .contact__list { list-style: none; margin-top: 9px; font-weight: 300; font-size: 16px; line-height: 20px; }
  .contact__item { display: flex; align-items: center; gap: 10px; }
  .contact__icon { width: 12px; height: 12px; flex: none; }
</style>
</head>
<body>
  <section class="card card--front">
    <div class="front__brand-side">
      <div class="brand brand--dark">
        <div class="brand__square"></div>
        <div class="brand__name">TKV VENTURES NZ LTD</div>
      </div>
    </div>
    <div class="front__info-side">
      <div class="front__notch"></div>
      <div class="contact">
        <h1 class="contact__name">HOWARD PENNICK</h1>
        <p class="contact__role">Director</p>
        <p class="contact__address">PO BOX 48215<br>Devonport Auckland<br>New Zealand</p>
        <ul class="contact__list">
          <li class="contact__item">
            <svg class="contact__icon" viewBox="0 0 12 12" aria-hidden="true"><path d="M3 1.2 L4.6 3.4 L3.7 4.5 Q4.6 6.6 6.6 7.8 L7.7 6.9 L9.8 8.5 L8.8 10.2 Q4.6 10 2 5 Q1.8 2.3 3 1.2 Z" fill="none" stroke="#fff" stroke-width="1"/></svg>
            <span>+64 21 843 192</span>
          </li>
          <li class="contact__item">
            <svg class="contact__icon" viewBox="0 0 12 12" aria-hidden="true"><rect x="1" y="3" width="10" height="6.5" fill="none" stroke="#fff" stroke-width="1"/><path d="M1 3 L6 7 L11 3" fill="none" stroke="#fff" stroke-width="1"/></svg>
            <span>hdpennick@fernmail.co.nz</span>
          </li>
          <li class="contact__item">
            <svg class="contact__icon" viewBox="0 0 12 12" aria-hidden="true"><circle cx="6" cy="6" r="4.8" fill="none" stroke="#fff" stroke-width="0.9"/><ellipse cx="6" cy="6" rx="2" ry="4.8" fill="none" stroke="#fff" stroke-width="0.9"/><path d="M1.2 6 H10.8 M2 3.6 H10 M2 8.4 H10" stroke="#fff" stroke-width="0.8"/></svg>
            <span>www.tkvventuresnz.co.nz</span>
          </li>
        </ul>
      </div>
    </div>
  </section>

  <section class="card card--back">
    <div class="brand brand--light">
      <div class="brand__square"></div>
      <div class="brand__name">TKV VENTURES NZ LTD</div>
    </div>
  </section>
</body>
</html>
```